Tidal Crumb Ingredients

Ingredients list/einkorn info. We are looking to improve a 5.5 x 8.5" double sided handout (2 per 8.5 x 11" piece of paper) to hand out with bread and for marketing. Or skinnier 3 per piece of paper? Or suggest a better format. Also to be used in social media and web. And possibly a banner.

Target Market(s)

Healthy, intelligent, yoga, athletic, wealthy

Industry/Entity Type

Bakery

Font styles to use
Sans Serif
Other font styles liked:
• simple readable attractive

Requirements
Must have
• Display the value (and uniqueness) of ingredients
Nice to have
• Well presented info with instant visual appeal. Choose between the 2 logos which you like most. Let us know if you want more photos.
Should not have
• Ornate frills

```html
<!DOCTYPE html>
<html lang="en">
<head>
<meta charset="utf-8">
<title>Tidal Crumb – Einkorn Handout</title>
<link href="https://fonts.googleapis.com/css2?family=Merriweather:wght@700;900&family=Raleway:wght@400;500;600;700&display=swap" rel="stylesheet">
<style>
:root{
  --stage:#a9a9a9;
  --cream:#f1e4d8;
  --cream-deep:#e6d3c1;
  --white:#ffffff;
  --brown:#8d5a2e;
  --brown-light:#b98554;
  --blue:#0d4ea0;
  --green:#6aa843;
  --ink:#2b2320;
  --body:#3a3330;
}
*{margin:0;padding:0;box-sizing:border-box}
html,body{width:1200px;height:1117px;overflow:hidden;background:var(--stage)}
body{position:relative;font-family:"Raleway",sans-serif;color:var(--body)}
.page{position:absolute;top:212px;width:536px;height:693px;background:var(--cream);overflow:hidden;box-shadow:4px 6px 10px rgba(0,0,0,.25)}
.page--front{left:52px}
.page--back{left:613px}
.page__sheet{position:absolute;left:13px;top:13px;right:13px;bottom:13px;background:var(--white)}
.swoosh{position:absolute;left:0;top:0;width:536px;height:693px}
.abs{position:absolute}
.photo{position:absolute;background:linear-gradient(135deg,#c99363,#a8693d 55%,#8a5230);border-radius:10px}
.brand{position:absolute;display:flex;align-items:center;gap:8px;font-family:"Merriweather",serif;font-weight:700;color:var(--blue);font-size:22px;white-space:nowrap}
.brand__dot{width:14px;height:14px;border-radius:50%;background:var(--green)}
.headline-small{font-family:"Merriweather",serif;font-weight:700;color:var(--green);font-size:19px;text-align:center;line-height:1}
.headline-big{font-family:"Merriweather",serif;font-weight:900;color:var(--blue);font-size:84px;line-height:1;letter-spacing:-1px}
.pillars{left:0;width:536px;top:360px;text-align:center;font-family:"Merriweather",serif;font-weight:700;font-size:23px;color:var(--ink)}
.pillars .sep{color:var(--green);font-size:16px;vertical-align:middle;margin:0 9px}
.tagline{left:0;width:536px;top:395px;text-align:center;font-weight:700;font-size:12.5px;color:var(--brown)}
.ingredients{left:46px;top:422px;width:443px;height:167px;border:2px solid var(--brown);border-radius:12px;background:var(--white);box-shadow:5px 5px 0 var(--cream-deep)}
.ingredients h3{font-family:"Merriweather",serif;font-weight:700;font-size:13.5px;color:var(--blue);margin-bottom:2px}
.ingredients p{font-size:10.8px;line-height:1.22;color:var(--body)}
.ingredients .fine{font-size:7.6px;line-height:1.2;margin-top:3px}
.ingredients .group{position:absolute}
.rule-h{position:absolute;border-top:1px dashed #9a9a9a}
.rule-v{position:absolute;border-left:1px dashed #9a9a9a}
.tolerance{left:0;width:536px;top:605px;text-align:center;font-family:"Merriweather",serif;font-weight:700;font-size:13.6px;color:var(--ink)}
.tolerance small{display:block;font-family:"Raleway",sans-serif;font-weight:400;font-size:12px;color:var(--body);margin-top:1px}
.contact{position:absolute;bottom:0;height:42px;left:93px;width:349px;background:var(--green);clip-path:polygon(5% 0,95% 0,100% 100%,0 100%);border-radius:16px 16px 0 0;color:var(--white);font-weight:600;font-size:13.5px;display:flex;align-items:center;justify-content:center;gap:8px}
.contact svg{width:12px;height:12px;vertical-align:-1px;margin-right:3px}
.contact .bar{opacity:.8;font-weight:400}
.title{left:0;width:536px;top:40px;text-align:center;font-family:"Merriweather",serif;font-weight:700;color:var(--blue);font-size:28px}
.title span{color:var(--green);font-size:22px}
.intro{left:0;width:536px;top:80px;text-align:center;font-size:14px;line-height:1.15;color:var(--ink)}
.pill{left:57px;top:128px;width:393px;height:25px;border-radius:13px;background:var(--blue);color:var(--white);font-family:"Merriweather",serif;font-weight:700;font-size:16px;text-align:center;line-height:25px}
.facts{left:56px;top:167px;width:400px;list-style:none}
.facts li{position:relative;padding-left:19px;font-size:10.8px;line-height:16.6px;color:var(--body)}
.facts li svg{position:absolute;left:0;top:4px;width:11px;height:9px}
.claim{left:0;width:536px;top:358px;text-align:center;font-family:"Merriweather",serif;font-weight:700;font-size:17px;line-height:1.18;color:var(--ink)}
.claim span{color:var(--green)}
</style>
</head>
<body>

<!-- FRONT -->
<section class="page page--front">
  <div class="page__sheet"></div>
  <svg class="swoosh" viewBox="0 0 536 693" aria-hidden="true">
    <path d="M0 240 C40 300 120 320 200 318 C300 314 420 300 480 340 C520 370 536 420 536 470 L536 693 L0 693 Z" fill="var(--cream)"/>
    <path d="M0 240 C40 300 120 320 200 318 C300 314 420 300 480 340 C520 370 536 420 536 470 L536 440 C530 390 500 345 450 325 C380 300 280 312 190 310 C110 308 40 290 0 250 Z" fill="var(--brown)"/>
    <path d="M0 275 C50 320 130 332 210 330 C300 326 420 318 480 356 C515 380 530 420 536 470 L536 693 L0 693 Z" fill="var(--white)"/>
    <path d="M0 590 C60 520 200 470 380 470 C460 470 510 440 536 410 L536 693 L0 693 Z" fill="var(--cream)" opacity=".8"/>
    <path d="M0 640 C120 600 300 610 536 600 L536 693 L0 693 Z" fill="var(--cream-deep)" opacity=".7"/>
  </svg>

  <div class="photo" role="img" aria-label="Photo of three stacked slices of swirled einkorn bread" style="left:40px;top:40px;width:210px;height:300px;transform:rotate(-8deg)"></div>

  <div class="brand" style="left:338px;top:98px"><span class="brand__dot"></span>Tidal Crumb</div>

  <div class="abs headline-small" style="left:290px;width:200px;top:203px">The</div>
  <div class="abs headline-small" style="left:280px;width:220px;top:222px">Transformation of</div>
  <div class="abs headline-big" style="left:267px;top:230px">bread</div>

  <div class="abs pillars">Nutritious<span class="sep">●</span>digestible<span class="sep">●</span>delicious</div>
  <div class="abs tagline">An alternative to the mutated genetics of modern wheat</div>

  <div class="abs ingredients">
    <div class="group" style="left:18px;top:12px;width:195px">
      <h3>Sprouted grains:</h3>
      <p>Einkorn, spelt, and a touch of heritage rye (Organically grown on family farms in Winthrop, Washington and Teton Valley, Idaho)</p>
    </div>
    <div class="rule-h" style="left:20px;top:99px;width:188px"></div>
    <div class="group" style="left:19px;top:110px;width:195px">
      <h3>Adaptogens:</h3>
      <p>Ashwaganda, Maca root</p>
    </div>
    <div class="rule-v" style="left:223px;top:18px;height:130px"></div>
    <div class="group" style="left:240px;top:14px;width:190px">
      <h3>Seeds:</h3>
      <p>Amaranth, sprouted pumpkin seeds, sprouted quinoa, chia seeds, flaxseed, hemp hearts, sprouted sunflowers seeds</p>
    </div>
    <div class="rule-h" style="left:240px;top:87px;width:181px"></div>
    <div class="group" style="left:240px;top:94px;width:190px">
      <h3>Mushroom extracts:</h3>
      <p>Lions mane, cordycept</p>
      <p class="fine">With: Montana glacier well water, Cacao, MCT oil, psyllium husk, Himalayan sea salt, trace minerals,&nbsp; love</p>
    </div>
  </div>

  <div class="abs tolerance">This bread is well tolerated by people with gluten sensitivities.<small>(not for celiac disease)</small></div>

  <div class="contact">
    <span><svg viewBox="0 0 12 12"><circle cx="6" cy="6" r="6" fill="#fff"/><path d="M3.8 3.2l1.1-.3.6 1.4-.7.5c.3.8.9 1.4 1.7 1.7l.5-.7 1.4.6-.3 1.1c-2.4.1-4.4-1.9-4.3-4.3z" fill="var(--green)"/></svg>406-555-0182</span>
    <span class="bar">|</span>
    <span><svg viewBox="0 0 12 12"><rect x=".5" y="2" width="11" height="8" fill="none" stroke="#fff"/><path d="M.5 2l5.5 4.5L11.5 2" fill="none" stroke="#fff"/></svg>hello@tidalcrumb.com</span>
  </div>
</section>

<!-- BACK -->
<section class="page page--back">
  <div class="page__sheet"></div>
  <svg class="swoosh" viewBox="0 0 536 693" aria-hidden="true">
    <path d="M0 380 C60 330 200 330 300 335 C420 340 500 320 536 280 L536 693 L0 693 Z" fill="var(--cream)"/>
    <path d="M200 460 C330 440 480 420 536 340 L536 380 C490 440 360 458 220 470 Z" fill="var(--brown)"/>
    <path d="M230 475 C360 462 490 440 536 385 L536 693 L230 693 Z" fill="var(--cream-deep)" opacity=".8"/>
    <path d="M320 493 C400 480 490 465 536 440 L536 693 L320 693 Z" fill="var(--white)"/>
  </svg>

  <div class="abs title">Einkorn grain vs <span>'modern wheat'</span></div>
  <div class="abs intro">Einkorn is the original, non-altered wheat grain.<br>It's genetic purity is over 10,000 years old.</div>
  <div class="abs pill">Einkorn is:</div>

  <ul class="abs facts">
    <li><svg viewBox="0 0 11 9"><path d="M1 4.5l3 3L10 1" fill="none" stroke="var(--brown)" stroke-width="2"/></svg>25% higher in protein and lower in carbohydrates than modern wheat</li>
    <li><svg viewBox="0 0 11 9"><path d="M1 4.5l3 3L10 1" fill="none" stroke="var(--brown)" stroke-width="2"/></svg>3-4 times more beta-carotene</li>
    <li><svg viewBox="0 0 11 9"><path d="M1 4.5l3 3L10 1" fill="none" stroke="var(--brown)" stroke-width="2"/></svg>2 times more vitamin A</li>
    <li><svg viewBox="0 0 11 9"><path d="M1 4.5l3 3L10 1" fill="none" stroke="var(--brown)" stroke-width="2"/></svg>4 times more antioxidants lutein and riboflavin.</li>
    <li><svg viewBox="0 0 11 9"><path d="M1 4.5l3 3L10 1" fill="none" stroke="var(--brown)" stroke-width="2"/></svg>5-6 times more expensive $$$</li>
    <li><svg viewBox="0 0 11 9"><path d="M1 4.5l3 3L10 1" fill="none" stroke="var(--brown)" stroke-width="2"/></svg>richer in carotenoids, B vitamins, and essential and trace minerals</li>
    <li><svg viewBox="0 0 11 9"><path d="M1 4.5l3 3L10 1" fill="none" stroke="var(--brown)" stroke-width="2"/></svg>non-processed, non-hybridized, non-GMO, non-&nbsp; mutated and has a low glycemic load, meaning it won't spike your blood sugar level.</li>
    <li><svg viewBox="0 0 11 9"><path d="M1 4.5l3 3L10 1" fill="none" stroke="var(--brown)" stroke-width="2"/></svg>and it tastes better.</li>
  </ul>

  <div class="abs claim"><span>Einkorn</span> lacks the gluten proteins that trigger<br>symptoms of gluten sensitivity.</div>

  <div class="photo" role="img" aria-label="Close-up photo of a single slice of swirled einkorn bread" style="left:-10px;top:410px;width:320px;height:300px;border-radius:30px 60px 0 0;transform:rotate(-6deg)"></div>

  <div class="brand" style="left:352px;top:537px"><span class="brand__dot"></span>Tidal Crumb</div>

  <div class="contact" style="left:94px">
    <span><svg viewBox="0 0 12 12"><circle cx="6" cy="6" r="6" fill="#fff"/><path d="M3.8 3.2l1.1-.3.6 1.4-.7.5c.3.8.9 1.4 1.7 1.7l.5-.7 1.4.6-.3 1.1c-2.4.1-4.4-1.9-4.3-4.3z" fill="var(--green)"/></svg>406-555-0182</span>
    <span class="bar">|</span>
    <span><svg viewBox="0 0 12 12"><rect x=".5" y="2" width="11" height="8" fill="none" stroke="#fff"/><path d="M.5 2l5.5 4.5L11.5 2" fill="none" stroke="#fff"/></svg>hello@tidalcrumb.com</span>
  </div>
</section>

</body>
</html>
```